Investor Services
Zielgruppe
Unsere Broschüre richtet sich an Investoren und Kapitalanleger, die Ihre Ferienwohnung nicht selbst nutzen und gut vermarktet wissen wollen. Die Broschüre soll für unser Unternehmen 'Sonnenklare Tage Ihre Urlaubsverwalter' als Akquisehilfsmittel genutzt werden. Sonnenklare Tage Ihre Urlaubsverwalter vermietet hochwertige Ferienwohnungen in Greetsiel und auf Ameland. Zielgruppe sind Endkunden, wie Familien mit und ohne Kinder, Paare, Paare mit und ohne Hund, Alleinreisende mit und ohne Hund - alle mittleren Alters.
Aufgabenstellung
Achtung Änderung: Ich habe den Eindruck, dass die von uns hochgeladene Version für den Umfang nur verwirrt und habe aus dem Grund jetzt die Datei gelöscht und die reinen Texte hochgeladen!
Wir lieben verschwenderische Gestaltung mit viel Freiraum. Die Texte sollen nicht auf wenige Seiten gequetscht werden. Ein quadratisches Format von 20*20 finden wir gut, ist aber keine feste Vorgabe. Auch können wir uns ein Format in 20*25 vorstellen, mal etwas, was anders ist aber auch keine feste Vorgabe. Wir fügen Ihnen die groben Texte, die in einem Ansichtslayout sind (bitte Typo und Gestaltung überhaupt nicht beachten, es ist nur eine Skizze, um eine Idee von Aufbau und Umfang zu bekommen) bei - mit den Texten ist es ggfs. einfacher, Design und Format zu entscheiden. Ich habe weiterhin ein paar Fotos hochgeladen, auch nur zur Ansicht, damit Sie wissen, was in etwa an Material da ist.
Gerne würden wir später im Druck die Broschüre veredeln - ggfs. mit einer Heißfolienprägung auf dem Titel, oder, wenn es das Design zulässt, auch im Inhalt.
Bitte beim Logo den Zusatz 'Ihre Fewovermieter' auswechseln gegen 'Investor Services'.

```html
<!DOCTYPE html>
<html lang="de">
<head>
<meta charset="utf-8">
<title>Sonnenklare Tage – Investor Services Broschüre</title>
<link href="https://fonts.googleapis.com/css2?family=Barlow+Semi+Condensed:wght@300;400;500&family=Open+Sans:wght@400;700&display=swap" rel="stylesheet">
<style>
  :root{
    --canvas:#ffffff;
    --stage:#f2f2f2;
    --paper:#ffffff;
    --ink:#2b2b2b;
    --muted:#8a8a8a;
    --brown:#5e544c;
    --line:#e2e2e2;
    --head:"Barlow Semi Condensed", Arial, sans-serif;
    --body:"Open Sans", Arial, sans-serif;
  }
  *{box-sizing:border-box;margin:0;padding:0}
  html,body{width:1200px;height:1200px;overflow:hidden;background:var(--canvas)}
  .board{position:relative;width:1200px;height:1200px}
  .panel{position:absolute;width:552px;height:359px;background:var(--stage)}
  .col-a{left:37px}.col-b{left:617px}
  .row-1{top:37px}.row-2{top:425px}.row-3{top:811px}

  .spread{position:absolute;left:37px;top:59px;width:469px;height:233px;display:flex;box-shadow:0 6px 14px rgba(0,0,0,.08)}
  .page{position:relative;width:50%;height:100%;background:var(--paper);overflow:hidden}
  .page.left{background:linear-gradient(to left,#ebebeb 0,#fff 14px)}
  .page.right{background:linear-gradient(to right,#e6e6e6 0,#fff 12px)}
  .folio{position:absolute;font-family:var(--body);font-size:3px;color:var(--ink);top:19px;left:45px;border-top:.5px solid var(--ink);padding-top:1px;width:5px}
  .folio.bottom{top:auto;bottom:44px;left:16px}

  .photo{position:absolute}
  .h2{font-family:var(--head);font-weight:500;font-size:7px;letter-spacing:.4px;color:var(--ink);text-transform:uppercase;line-height:1}
  .h2 small{display:block;font-weight:400;font-size:4.6px;color:var(--muted);margin-top:1px}
  .copy{position:absolute;font-family:var(--body);font-size:3.2px;line-height:5.4px;color:var(--ink)}
  .copy p{margin-bottom:4px}
  .copy b{font-weight:700}
  .justify{text-align:justify}

  /* cover */
  .cover{position:absolute;left:169px;top:72px;width:214px;height:215px;background:var(--paper);box-shadow:0 6px 14px rgba(0,0,0,.12)}
  .cover .photo{left:0;top:27px;width:214px;height:135px;background:linear-gradient(180deg,#2f74c4 0%,#5aa4e0 45%,#9fd0ea 58%,#e6e4df 72%,#d7d2c8 100%)}
  .cover-title{position:absolute;left:0;right:0;top:52px;text-align:center;color:#fff;font-family:var(--head)}
  .cover-title .l1{font-weight:300;font-size:11.5px;letter-spacing:.5px}
  .cover-title .l2{font-weight:500;font-size:7.4px;letter-spacing:.6px;margin-top:2px}
  .cover-title .q{font-size:12px;font-weight:500;vertical-align:-3px;margin-right:3px}
  .brand{position:absolute;left:0;right:0;top:177px;text-align:center;font-family:var(--head);color:#8c8c8c}
  .brand .name{font-size:8px;font-weight:400;letter-spacing:.4px}
  .brand .tag{font-size:3px;letter-spacing:.6px;margin-top:1px}

  /* contents */
  .toc{position:absolute;left:45px;right:0;height:45px;background:var(--brown);color:#fff;display:flex;align-items:center;justify-content:space-between;padding:0 13px 0 12px}
  .toc .t{font-family:var(--head);font-weight:500;font-size:6.2px;letter-spacing:.4px}
  .toc .s{font-family:var(--body);font-size:2.6px;color:#d6d0ca;margin-top:2px}
  .toc .n{font-family:var(--head);font-weight:400;font-size:21px}

  /* icon rows */
  .icons{position:absolute;left:45px;font-family:var(--body);font-size:2.8px;line-height:3.8px;color:var(--ink)}
  .icons li{list-style:none;display:flex;align-items:center;gap:7px;margin-bottom:9px}
  .icons svg{width:11px;height:11px;flex:none}

  .signature{position:absolute;left:45px;top:190px;font-family:var(--head);font-weight:400;font-size:10px;color:var(--ink)}
  .quote{position:absolute;font-family:var(--head);font-weight:300;color:#fff;font-size:5.6px;line-height:7px;letter-spacing:.2px}
  .quote .mark{font-weight:500;font-size:13px;line-height:8px;display:block}
</style>
</head>
<body>
<main class="board">

  <!-- Cover -->
  <section class="panel col-a row-1">
    <div class="cover">
      <div class="photo" role="img" aria-label="Titelfoto: offene Terrasse einer Ferienvilla mit Blick auf das türkisblaue Meer"></div>
      <div class="cover-title">
        <div class="l1">IM SCHÖNSTEN URLAUB,</div>
        <div class="l2"><span class="q">“</span>ARBEITET NUR IHR GELD.</div>
      </div>
      <div class="brand">
        <div class="name">Sonnenklare Tage</div>
        <div class="tag">INVESTOR SERVICES</div>
      </div>
    </div>
  </section>

  <!-- Portrait -->
  <section class="panel col-b row-1">
    <div class="spread">
      <div class="page left">
        <div class="photo" role="img" aria-label="Foto: Hund sitzt aufrecht in einer hellen Ferienwohnung" style="left:69px;top:14px;width:165px;height:205px;background:linear-gradient(135deg,#e9e6e0 0%,#d8cfc2 40%,#b58a5e 70%,#c9b9a6 100%)"></div>
        <div class="folio bottom">2</div>
      </div>
      <div class="page right">
        <div class="folio">3</div>
        <div class="h2" style="position:absolute;left:45px;top:64px">Sonnenklare Tage<small>EIN PORTRAIT</small></div>
        <div class="copy" style="left:45px;top:88px;width:145px">
          <p>Sonnenklare Tage ist ein <b>Familienunternehmen</b> – gegründet und geführt von zwei erfolgreichen Unternehmern, die schönen Urlaub lieben und exzellenten Service.</p>
          <p>Wir gönnen uns den Luxus, unseren Besuchern eine handverlesene Auswahl an Wohnungen anzubieten, in denen wir selbst gerne unsere Zeit verbringen möchten. Wir sichern <b>Qualität durch kompromisslos hohe Standards.</b></p>
          <p>Seit Jahren besitzen wir eigene Ferienwohnungen, die wir selbst finanziert, geplant und gestaltet haben. Heute bieten wir einen Rundum-Service an – von der Akquise bis zur Steigerung des Marktwertes.</p>
          <p>Dabei sind unsere Partner so handverlesen wie unsere Wohnungen und Gäste.</p>
        </div>
      </div>
    </div>
  </section>

  <!-- Contents -->
  <section class="panel col-a row-2">
    <div class="spread">
      <div class="page left"><div class="folio bottom">4</div></div>
      <div class="page right">
        <div class="folio">5</div>
        <div class="toc" style="top:45px"><div><div class="t">DIE GRUNDPFEILER UNSERES ERFOLGS</div><div class="s">Handverlesene Objekte — Erfahrung — Kluges Marketing — Persönlicher Kontakt</div></div><div class="n">08</div></div>
        <div class="toc" style="top:94px"><div><div class="t">WAS ICH IHNEN ANBIETE</div><div class="s">Akquise — Verwaltung — Innenausstattung — Wohnraumgestaltung — Verantwortung</div></div><div class="n">14</div></div>
        <div class="toc" style="top:143px"><div><div class="t">WAS MIR WICHTIG IST</div><div class="s">Wirtschaftlicher Erfolg — Klarheit — Vertrauen — Offenheit</div></div><div class="n">22</div></div>
      </div>
    </div>
  </section>

  <!-- Personal letter -->
  <section class="panel col-b row-2">
    <div class="spread">
      <div class="page left">
        <div class="photo" role="img" aria-label="Porträtfoto der Inhaberin am Meer" style="left:16px;top:14px;width:218px;height:153px;background:linear-gradient(90deg,#d6dbdd 0%,#c9c2b2 35%,#b3b1ad 60%,#dfe3e4 100%)"></div>
        <div class="copy" style="left:60px;top:183px;width:120px;font-size:2.9px;line-height:4.6px">Seit vielen Jahren entscheide ich mich bewusst, meinen Erfolg direkt von der Zufriedenheit meiner Kunden abhängig zu machen – jeden Tag. <b>Der Charakter von Vertrieb. Meine Königsdisziplin.</b></div>
        <div class="folio bottom">6</div>
      </div>
      <div class="page right">
        <div class="folio" style="left:214px;top:40px">7</div>
        <div class="copy" style="left:45px;top:38px;width:143px">
          <p>Meine Liebe zu schönen Ferien war immer groß. Dabei ging es weniger um Luxus und Chic – ich wollte den perfekten Raum für Ruhe und Erholung. Irgendwann haben wir diesen Raum selbst geschaffen.</p>
          <p>Ich arbeite gerne mit Gleichgesinnten, die mit mir gemeinsam <b>hohe Ziele</b> stecken. Vertrauen gewinnen und langfristigen Erfolg sichern. Ein Muss.</p>
          <p>Ich bin <b>Perfektionistin aus Überzeugung.</b> Perfekte Orte liebe ich genauso sehr wie perfekte Organisation, Ordnung und Klarheit. Meine Prozesse sind transparent, effizient und schlank.</p>
          <p>Gemeinsame unternehmerische Werte und Vertrauen sind mir wichtig. Ob die Chemie stimmt?</p>
          <p>Ich freue mich auf Sie und Ihr Objekt.<br>Herzlich,</p>
        </div>
        <div class="signature">Meike Andersen</div>
      </div>
    </div>
  </section>

  <!-- Services -->
  <section class="panel col-a row-3">
    <div class="spread">
      <div class="page left">
        <div class="h2" style="position:absolute;left:45px;top:61px">Akquise<small>WAS ICH IHNEN ANBIETE</small></div>
        <div class="copy justify" style="left:45px;top:83px;width:142px">Wir kümmern uns um eine optimale Buchungsrate für jedes unserer Objekte. Wir sind nicht auf jedem Portal vertreten, die sich für Qualität statt Quantität entscheiden. Dafür bekommt jeder Kundenwunsch unsere volle Aufmerksamkeit. Wir haben eine Umwandlungsquote von 85%.</div>
        <ul class="icons" style="top:140px">
          <li><svg viewBox="0 0 12 12" fill="none" stroke="#444" stroke-width=".7"><rect x="1" y="2" width="9" height="6"/><circle cx="8" cy="8" r="2.2"/><line x1="9.6" y1="9.6" x2="11" y2="11"/></svg>Die Website www.sonnenklaretage.de ist an die<br>wichtigsten Portale angeschlossen.</li>
          <li><svg viewBox="0 0 12 12" fill="none" stroke="#444" stroke-width=".7"><rect x="2" y="1" width="5" height="10" rx="1"/><rect x="7" y="4" width="4" height="3"/></svg>Wir reagieren auf jede Anfrage schnell,<br>konkret und individuell.</li>
          <li><svg viewBox="0 0 12 12" fill="none" stroke="#444" stroke-width=".7"><circle cx="4" cy="4" r="2"/><path d="M1 11c0-3 6-3 6 0"/><rect x="7" y="2" width="4" height="3"/></svg>Wir nehmen persönlich Kontakt zu Interessenten auf.</li>
        </ul>
        <div class="folio bottom">8</div>
      </div>
      <div class="page right">
        <div class="folio">9</div>
        <div class="h2" style="position:absolute;left:45px;top:61px">Verwaltung<small>WAS ICH IHNEN ANBIETE</small></div>
        <div class="copy justify" style="left:45px;top:83px;width:145px">Durch unsere Routine, optimale Prozesse, ein professionelles Buchungssystem und unsere Ordnungsliebe sind wir perfekt organisiert. Unser Anspruch ist hoch. Unser Ziel: Ein spürbar exklusiver Service, mit dem die Vorfreude auf den Urlaub direkt beginnt. Die Buchung der Vorauszahlungen auf das Eigentümer-Konto ist Standard.</div>
        <ul class="icons" style="top:158px">
          <li><svg viewBox="0 0 12 12" fill="none" stroke="#444" stroke-width=".7"><rect x="2" y="1" width="8" height="10"/><line x1="4" y1="4" x2="8" y2="4"/><line x1="4" y1="6" x2="8" y2="6"/><line x1="4" y1="8" x2="7" y2="8"/></svg>Wir setzen auf ein zuverlässiges Buchungssystem,<br>das Fehler ausschließt.</li>
          <li><svg viewBox="0 0 12 12" fill="none" stroke="#444" stroke-width=".7"><circle cx="6" cy="7" r="4"/><line x1="6" y1="5" x2="6" y2="9"/><path d="M4 2h4"/></svg>Wir geben Investoren einen Vertrauensvorschuss durch<br>Vorauszahlungen direkt auf das Eigentümer-Konto.</li>
        </ul>
      </div>
    </div>
  </section>

  <!-- Image spread -->
  <section class="panel col-b row-3">
    <div class="spread">
      <div class="page left"></div>
      <div class="page right"></div>
      <div class="photo" role="img" aria-label="Foto: helle Ferienwohnung mit Essbereich, Sitzbank und Kissen" style="left:16px;top:14px;width:452px;height:205px;background:linear-gradient(180deg,#e8e6e2 0%,#b9b6b1 45%,#a8a39c 62%,#8c7766 80%,#a08a78 100%)"></div>
      <div class="quote" style="left:299px;top:22px;width:80px">Sie stecken den finanziellen Rahmen. Ich kümmere mich um den Rest – mit viel Wissen und einer großen Prise Liebe.<span class="mark" style="padding-left:36px;margin-top:3px">”</span></div>
      <div class="quote" style="left:53px;top:154px;width:78px"><span class="mark">“</span>Ein Ferienhaus bringt eine gute Rendite, wenn es das Potenzial hat, für jeden Gast zum Herzstück eines Traumurlaubs zu werden.</div>
    </div>
  </section>

</main>
</body>
</html>
```